Bride Basecamp

I am looking for a design for http://www.bridebasecamp.co.uk/ its a joomla site and I am going to set up with the same mods as our stag version http://www.groomnightout.co.uk/ you will see on groomnight how all the menus look and are positioned. Here is an example of a activity page http://www.groomnightout.co.uk/activity/white-water-rafting-in-perthshire.html which comes from Kiln.

The design needs to be built for responsive layout. The brand look and feel needs to be 100% for the female market.

We can accept the design in photoshop or something similar

Please ask questions if you require more information.

some examples of hen sites

http://www.maidenmerry.co.uk/

```html
<!DOCTYPE html>
<html lang="en">
<head>
<meta charset="utf-8">
<title>Bride Basecamp</title>
<link href="https://fonts.googleapis.com/css2?family=Open+Sans:ital,wght@0,400;0,600;1,400&family=Arimo:ital,wght@0,400;1,400&display=swap" rel="stylesheet">
<style>
:root{
  --bg:#3b3b3b;
  --panel:#2f2f2f;
  --panel-dark:#2a2a2a;
  --accent:#ef7d12;
  --accent-frame:#c7640f;
  --nav:#1c1c1c;
  --text:#e6e6e6;
  --muted:#cfcfcf;
  --link:#8fb3ea;
  --star:#f5a300;
}
*{box-sizing:border-box;margin:0;padding:0}
html,body{width:879px;height:1200px;overflow:hidden}
body{
  position:relative;
  font-family:"Open Sans",sans-serif;color:var(--text);
  background:
    radial-gradient(ellipse 420px 300px at 790px 60px,rgba(180,80,55,.55),transparent 70%),
    linear-gradient(180deg,#4a4544 0%,var(--bg) 35%,#333 100%);
}
.abs{position:absolute}
.brand{left:123px;top:36px;font-size:19px;font-weight:600;letter-spacing:1px;color:#f2f2f2;text-transform:uppercase}
.social-top{left:484px;top:41px;display:flex;gap:6px}
.social-top span{width:17px;height:17px;border-radius:50%;background:#8a8a8a}
.search{left:596px;top:40px;width:156px;height:21px;background:#fff;font-size:10px;color:#888;padding:3px 10px}
.search svg{position:absolute;right:6px;top:4px}
.nav{left:123px;top:84px;width:628px;height:36px;background:var(--nav);display:flex}
.nav a{display:flex;align-items:center;justify-content:center;color:#fff;text-decoration:none;font-size:11px;text-transform:uppercase;border-right:1px solid #333}
.nav a.active{background:var(--accent)}
.hero{left:123px;top:125px;width:628px;height:252px;
  background:radial-gradient(circle at 20% 20%,#3aa6e8 0,transparent 35%),radial-gradient(circle at 80% 30%,#d8508e 0,transparent 40%),linear-gradient(120deg,#1c3d74,#8a3a5a 50%,#c46a50)}
.hero-caption{left:123px;top:314px;width:343px;height:39px;background:rgba(60,60,60,.75);color:#fff;font-family:"Arimo",sans-serif;font-size:18px;padding:8px 11px}
.dots{left:706px;top:361px;display:flex;gap:3px}
.dots span{width:5px;height:5px;border-radius:50%;background:#fff}
.welcome{left:123px;top:400px;width:628px;height:181px;background:var(--panel)}
.welcome h1{position:absolute;left:15px;top:18px;font-size:16px;font-weight:400;color:var(--accent)}
.welcome p{position:absolute;left:14px;width:340px;font-size:8.3px;line-height:14.5px;color:var(--muted)}
.video{left:518px;top:425px;width:220px;height:132px;background:linear-gradient(135deg,#4d3a5c,#a46b74 50%,#2c2434);box-shadow:0 1px 3px #000}
.video .bar{position:absolute;left:0;bottom:0;width:100%;height:14px;background:#111}
.tile{width:141px;height:122px;border:4px solid var(--accent-frame)}
.tile span{position:absolute;left:0;bottom:0;width:100%;height:24px;background:rgba(40,40,40,.6);color:#fff;font-size:11.5px;font-weight:600;padding:4px 8px}
.reviews{left:123px;top:901px;width:628px;height:184px;background:var(--panel)}
.reviews h2{position:absolute;left:14px;top:18px;font-size:16px;font-weight:400;color:var(--accent)}
.review{position:absolute;top:60px;width:125px;font-family:"Arimo",sans-serif}
.review h3{font-size:11px;font-weight:400;color:var(--link)}
.review .stars{color:var(--star);font-size:11px;letter-spacing:1px;margin:2px 0 6px}
.review p{font-size:8.3px;line-height:13px;color:#ddd}
.review em{display:block;text-align:right;font-size:8.3px;margin-top:3px;color:#ddd}
.footer{left:123px;top:1101px;width:628px;height:73px;background:var(--panel-dark);font-family:"Arimo",sans-serif;font-size:8.3px;color:#eee}
.footer .links{position:absolute;left:21px;top:21px}
.footer .copy{position:absolute;left:21px;top:43px}
.social-foot{position:absolute;left:480px;top:27px;display:flex;gap:8px}
.social-foot span{width:22px;height:22px;background:#6d6d6d}
</style>
</head>
<body>
<div class="abs brand">Bride Basecamp</div>
<div class="abs social-top"><span></span><span></span><span></span><span></span></div>
<div class="abs search">Search
  <svg width="11" height="11" viewBox="0 0 11 11"><circle cx="4.5" cy="4.5" r="3.3" fill="none" stroke="#222" stroke-width="1.6"/><line x1="7" y1="7" x2="10" y2="10" stroke="#222" stroke-width="2"/></svg>
</div>
<nav class="abs nav">
  <a class="active" style="width:75px">Home</a>
  <a style="width:113px">Locations</a>
  <a style="width:186px">European Destinations</a>
  <a style="width:101px">Contact</a>
  <a style="width:153px;border:0">Call 0181 555 0147</a>
</nav>
<div class="abs hero" role="img" aria-label="Group of women dancing at a party under colourful lights"></div>
<div class="abs hero-caption">DUIS AUTEM VEL EUM IRURE DOLOR</div>
<div class="abs dots"><span></span><span></span><span></span><span></span></div>

<section class="abs welcome">
  <h1>Welcome to Our Website</h1>
  <p style="top:56px">Eu tortor euismodolo. Vestibulum ant psu meop primis inicibu orci luctus edulue re cubil. Cura sed quis nibhut odiocinialor matis ed iaculis ante sed vel lacinieusm modolo. Vestibulum ant psu meop primis inicibu orci luctus ed ultrices etpCiurais ed quis nibhut odiocinialor matis ed iaculis ante sed vel laciniate.</p>
  <p style="top:117px">Eu tortor euismodolo. Vestibulum ant psu meop primis inicibu orci luctus eduluie re cubil. Cura sed quis nibhut odiocinialor matis ed iaculis ante sed vel lacineusm modolo. Vestibulum ant psu meop primis inicibu orci luctus ed ultrices.</p>
</section>
<div class="abs video" role="img" aria-label="Video of friends celebrating with cocktails">
  <svg class="abs" style="left:85px;top:40px" width="50" height="50" viewBox="0 0 50 50"><circle cx="25" cy="25" r="23" fill="rgba(0,0,0,.35)"/><path d="M19 14 L36 25 L19 36Z" fill="#eee"/></svg>
  <div class="bar">
    <svg width="220" height="14"><path d="M6 4 L10 7 L6 10Z" fill="#ddd"/><rect x="14" y="6" width="110" height="2" fill="#555"/><rect x="14" y="6" width="45" height="2" fill="#d33"/><text x="124" y="10" font-size="6" fill="#ddd" font-family="Arimo,sans-serif">1:26 / 3:22</text><rect x="165" y="6" width="20" height="2" fill="#d33"/><text x="203" y="10" font-size="6" fill="#ddd" font-family="Arimo,sans-serif" font-style="italic">HD</text></svg>
  </div>
</div>

<div class="abs tile" style="left:123px;top:608px;background:linear-gradient(#9fb0c8,#6f8a5a 45%,#3f6a2a)" role="img" aria-label="Green valley with mountains"><span>Aviewmore</span></div>
<div class="abs tile" style="left:285px;top:608px;background:linear-gradient(#e8eef2,#d9c54a 45%,#3a8fb8)" role="img" aria-label="Indoor water park pool"><span>Bournemouth</span></div>
<div class="abs tile" style="left:449px;top:608px;background:linear-gradient(#8fa6c4,#6b5a48 50%,#3a3240)" role="img" aria-label="Steam train on moorland"><span>Bristol</span></div>
<div class="abs tile" style="left:610px;top:608px;background:linear-gradient(#5d80b6,#c9d6e6 55%,#e8eef4)" role="img" aria-label="Snow covered rock in winter"><span>Silverade</span></div>
<div class="abs tile" style="left:123px;top:755px;background:linear-gradient(#3f7a3a,#c7c23a 50%,#6a7a2a)" role="img" aria-label="Rows of vines in a vineyard"><span>Manchestar</span></div>
<div class="abs tile" style="left:285px;top:755px;background:linear-gradient(#3a2a20,#3aa0b8 50%,#7a3a2a)" role="img" aria-label="Dancers in feathered costumes"><span>Bournemouth</span></div>
<div class="abs tile" style="left:449px;top:755px;background:linear-gradient(#8a8a8a,#e8ecf0 50%,#3a3a4a)" role="img" aria-label="Skiers on a snowy slope"><span>Bristol</span></div>
<div class="abs tile" style="left:610px;top:755px;background:linear-gradient(#8a929c,#5a6a6a 45%,#7aa04a)" role="img" aria-label="Meadow under cloudy mountains"><span>Silverade</span></div>

<section class="abs reviews">
  <h2>Customer Reviews</h2>
  <svg class="abs" style="left:595px;top:26px" width="22" height="14" viewBox="0 0 22 14"><path d="M7 2 L2 7 L7 12 M15 2 L20 7 L15 12" fill="none" stroke="var(--accent)" stroke-width="2"/></svg>
  <div class="review" style="left:14px"><h3>Excellant</h3><div class="stars">★★★★★</div><p>Duis auteim vel eumirurer heniin putaite velit esse. Cliaritas eetim pcessus. consuetudium lectoum</p><em>Amy Collins</em></div>
  <div class="review" style="left:173px"><h3>Friendly and Helpfull</h3><div class="stars">★★★★★</div><p>Duis auteim vel eumirurer heniin putaite velit esse. Cliaritas eetim pcessus. consuetudium lectoum</p><em>Amy Collins</em></div>
  <div class="review" style="left:335px"><h3>Friendly and Helpfull</h3><div class="stars">★★★★★</div><p>Duis auteim vel eumirurer heniin putaite velit esse. Cliaritas eetim pcessus. consuetudium lectoum</p><em>Amy Collins</em></div>
  <div class="review" style="left:491px"><h3>Friendly and Helpfull</h3><div class="stars">★★★★★</div><p>Duis auteim vel eumirurer heniin putaite velit esse. Cliaritas eetim pcessus. consuetudium lectoum</p><em>Amy Collins</em></div>
</section>

<footer class="abs footer">
  <div class="links">Terms and Conditions | Privacy Promise | FAQ's | Contact Us</div>
  <div class="copy">Copyright © 2013. All Rights Reserved.</div>
  <div class="social-foot"><span></span><span></span><span></span><span></span></div>
</footer>
</body>
</html>
```